Interior Design Company - Project Folder Design

Require simple layout design for company folders in a specific template as attach. Company name is MOVALT. Tag line is "make our visions alive, lasting, timeless" in Microsoft Word <Juice ITC> font type. Corporate colors include dark grey, turqoise and white.
Logo, AI template and some images are attached.

Company focus on Interior Design and Build services. Our services includes all commercial and residential projects.

Target Market(s)

B2B,B2C Corporate and Residential Design, Fit-outs and Project Management

Industry/Entity Type

Interior

Font styles to use
Sans Serif

Colors
33a6d7
333333
ffffff

Requirements
Must have
• Logo
• Address - No. 58 Kerrow Lane #04-21, Danvel Centre, Singapore 177492
• Web - www.movalt.com
Nice to have
• Clean professional architectural lines
Should not have
• No cartoons, kiddy images nor repetitive patterns

```html
<!DOCTYPE html>
<html lang="en">
<head>
<meta charset="utf-8">
<title>MOVALT Project Folder</title>
<link rel="stylesheet" href="https://fonts.googleapis.com/css2?family=Open+Sans:wght@300;400&display=swap">
<style>
  :root {
    --charcoal: #1f2427;
    --mint: #35e28c;
    --mint-deep: #2bb775;
    --paper: #ffffff;
    --dieline: rgba(255,255,255,0.75);
  }
  html, body { margin: 0; padding: 0; overflow: hidden; background: var(--paper); }
  .folder {
    position: relative;
    width: 1200px; height: 741px;
    overflow: hidden;
    background: var(--paper);
    font-family: "Open Sans", Arial, sans-serif;
  }
  .folder > * { position: absolute; }
  .top-band { left: 0; top: 0; width: 1200px; height: 218px; background: var(--charcoal); }
  .side-flap { left: 5px; top: 218px; width: 242px; height: 466px; background: var(--mint); }
  .bottom-flap { left: 5px; top: 684px; width: 705px; height: 51px; background: var(--mint); }
  .front-panel { left: 248px; top: 382px; width: 952px; height: 302px; background: var(--mint); }
  .gallery { left: 248px; top: 237px; width: 952px; height: 125px; display: flex; }
  .gallery .shot { height: 100%; }
  .shot-1 { width: 201px; background: linear-gradient(120deg, #8a6d55, #d9d4cc 55%, #f1efec); }
  .shot-2 { width: 167px; background: linear-gradient(160deg, #4b4a45, #c9c1ae 50%, #e8e4da); }
  .shot-3 { width: 188px; background: linear-gradient(170deg, #5b4d3c, #8a7a62 45%, #2e2a26); }
  .shot-4 { width: 198px; background: linear-gradient(130deg, #9a8c7d, #e6e6e4 55%, #cfc9c1); }
  .shot-5 { width: 198px; background: linear-gradient(150deg, #d8dde0, #3a3f44 50%, #e4e6e7); }
  .lines { left: 0; top: 0; width: 1200px; height: 741px; }
  .brand {
    right: 42px; top: 118px;
    text-align: right; color: var(--paper);
  }
  .brand-name {
    display: flex; align-items: center; justify-content: flex-end; gap: 12px;
    font-weight: 300; font-size: 46px; line-height: 1; letter-spacing: 2px;
  }
  .brand-mark { width: 12px; height: 12px; border: 1.5px solid var(--paper); }
  .tagline { margin-top: 14px; font-weight: 300; font-size: 14px; }
  .contact {
    left: 248px; top: 648px; width: 462px;
    text-align: center; color: var(--paper);
    font-size: 10px; line-height: 13px;
  }
  .contact p { margin: 0; }
</style>
</head>
<body>
<div class="folder">
  <div class="top-band"></div>
  <div class="side-flap"></div>
  <div class="bottom-flap"></div>
  <div class="front-panel"></div>

  <svg class="lines" viewBox="0 0 1200 741" aria-hidden="true">
    <polygon points="250,684 725,383 1190,684" fill="var(--mint-deep)"/>
    <g fill="none" stroke="var(--dieline)" stroke-width="1">
      <polyline points="10,40 22,10 220,10 232,40"/>
      <polyline points="10,700 22,730 220,730 232,700"/>
      <line x1="10" y1="57" x2="1200" y2="57"/>
      <line x1="10" y1="684" x2="1200" y2="684"/>
      <line x1="232" y1="57" x2="232" y2="700"/>
      <line x1="247" y1="57" x2="247" y2="684"/>
      <line x1="711" y1="57" x2="711" y2="735"/>
      <line x1="726" y1="57" x2="726" y2="684"/>
      <line x1="10" y1="40" x2="10" y2="57"/>
    </g>
  </svg>

  <div class="gallery">
    <div class="shot shot-1" role="img" aria-label="Living room interior with timber barn doors"></div>
    <div class="shot shot-2" role="img" aria-label="Lounge interior with feature shelving"></div>
    <div class="shot shot-3" role="img" aria-label="Living and dining area with decorative ceiling"></div>
    <div class="shot shot-4" role="img" aria-label="Bedroom with timber feature wall"></div>
    <div class="shot shot-5" role="img" aria-label="Open living room with dark shelving"></div>
  </div>

  <div class="brand">
    <div class="brand-name"><span class="brand-mark"></span>movalt</div>
    <div class="tagline">make our visions alive, lasting, timeless</div>
  </div>

  <div class="contact">
    <p>No. 58 Kerrow Lane #04-21, Danvel Centre, Singapore 177492</p>
    <p>www.movalt.com</p>
  </div>
</div>
</body>
</html>
```